Medical Company in need of Modern business card design for new Wound Care clinic.

Modern business card design for our Woundcare company. Logo and description of services can be found on our website; https://www.tovrel-woundcare.com/

```html
<!DOCTYPE html>
<html lang="en">
<head>
<meta charset="utf-8">
<title>Tovrel Woundcare – Business Card</title>
<link rel="stylesheet" href="https://fonts.googleapis.com/css2?family=Poppins:wght@500;600&family=Quicksand:wght@500;600&family=Josefin+Sans:wght@700&display=swap">
<style>
  :root {
    --bg: #e9e6e1;
    --card-white: #ffffff;
    --card-dark: #1f1c1c;
    --ink: #151515;
    --gold: #d39a2c;
    --gold-soft: #b98a3e;
    --text-light: #f2efe9;
  }
  * { margin: 0; padding: 0; box-sizing: border-box; }
  html, body {
    width: 1200px; height: 900px; overflow: hidden;
    background: var(--bg);
  }
  .stage {
    width: 1200px; height: 900px;
    display: flex; flex-direction: column; align-items: center; justify-content: center;
    gap: 34px;
  }
  .card {
    width: 700px; height: 400px;
    border-radius: 34px;
    position: relative;
    box-shadow: 0 10px 30px rgba(0,0,0,.15);
    overflow: hidden;
  }
  /* Front */
  .card--front {
    background: var(--card-white);
    display: flex; align-items: center; justify-content: center;
  }
  .brand {
    display: flex; align-items: center; gap: 22px;
  }
  .brand__mark {
    width: 30px; height: 30px; background: var(--gold);
  }
  .brand__name {
    font-family: "Poppins", sans-serif;
    font-weight: 500;
    font-size: 40px;
    letter-spacing: 9px;
    color: var(--ink);
  }
  /* Back */
  .card--back {
    background: var(--card-dark);
    color: var(--text-light);
  }
  .person {
    position: absolute; left: 48px; top: 196px;
  }
  .person__name {
    font-family: "Josefin Sans", sans-serif;
    font-weight: 700; font-size: 25px;
    color: var(--gold); letter-spacing: .5px;
  }
  .person__role {
    font-family: "Quicksand", sans-serif;
    font-weight: 500; font-size: 19px; margin-top: 2px;
  }
  .contact {
    position: absolute; left: 330px; top: 118px;
    list-style: none;
    font-family: "Quicksand", sans-serif; font-weight: 500; font-size: 18px;
  }
  .contact__item {
    display: flex; align-items: center; gap: 12px; height: 34px;
  }
  .contact__icon { width: 20px; height: 20px; flex: none; }
  .rule {
    position: absolute; left: 330px; right: 40px; top: 276px;
    height: 1px; background: var(--gold-soft);
  }
  .back-brand {
    position: absolute; left: 330px; top: 292px;
    font-family: "Poppins", sans-serif; font-weight: 500;
    font-size: 30px; letter-spacing: 7px; color: var(--gold);
  }
</style>
</head>
<body>
<main class="stage">
  <section class="card card--front" aria-label="Card front">
    <div class="brand">
      <span class="brand__mark"></span>
      <span class="brand__name">TOVREL WOUNDCARE</span>
    </div>
  </section>

  <section class="card card--back" aria-label="Card back">
    <div class="person">
      <div class="person__name">MARCUS HALE</div>
      <div class="person__role">Director</div>
    </div>

    <ul class="contact">
      <li class="contact__item">
        <svg class="contact__icon" viewBox="0 0 24 24" fill="var(--gold)"><path d="M6.6 10.8a15 15 0 0 0 6.6 6.6l2.2-2.2a1 1 0 0 1 1-.25 11.4 11.4 0 0 0 3.6.57 1 1 0 0 1 1 1V20a1 1 0 0 1-1 1A17 17 0 0 1 3 4a1 1 0 0 1 1-1h3.5a1 1 0 0 1 1 1c0 1.25.2 2.45.57 3.57a1 1 0 0 1-.25 1z"/></svg>
        <span>555-014-2286</span>
      </li>
      <li class="contact__item">
        <svg class="contact__icon" viewBox="0 0 24 24" fill="var(--gold)"><path d="M6 2h9l3 3v4H6z M3 10h18v8h-3v4H6v-4H3z M8 15v5h8v-5z"/></svg>
        <span>555-014-2287</span>
      </li>
      <li class="contact__item">
        <svg class="contact__icon" viewBox="0 0 24 24" fill="none" stroke="var(--gold)" stroke-width="1.8"><circle cx="12" cy="12" r="9"/><ellipse cx="12" cy="12" rx="4" ry="9"/><path d="M3 12h18M5 7h14M5 17h14"/></svg>
        <span>www.tovrel-woundcare.com</span>
      </li>
      <li class="contact__item">
        <svg class="contact__icon" viewBox="0 0 24 24" fill="var(--gold)"><path d="M12 2a7 7 0 0 0-7 7c0 5 7 13 7 13s7-8 7-13a7 7 0 0 0-7-7zm0 9.5A2.5 2.5 0 1 1 12 6.5a2.5 2.5 0 0 1 0 5z"/></svg>
        <span>4120 Birchwood Ave Bldg. C, suite 118</span>
      </li>
    </ul>

    <div class="rule"></div>
    <div class="back-brand">TOVREL WOUNDCARE</div>
  </section>
</main>
</body>
</html>
```